Velmora Diagnostics Website

Project Description – Velmora Website Design
We need a clean, modern, and professional website for Velmora Diagnostics, a Ashgrove Hollis University of Dunmere spin-out focused on early cancer detection. Our first product, GlandSURE™, is a urine-based risk assessment test for pancreatic cancer, supported by strong clinical validation and partnerships with leading hospitals.

The site should:

Communicate trust, innovation, and clinical credibility.
Feature a clear value proposition on the home page with strong calls to action for investors, clinicians, and partners.
Showcase our technology, science, and clinical evidence in a way that is accessible but authoritative.
Highlight our university heritage, team, and collaborators.
Include sections for products/services, news/press, and contact forms.
Be fully responsive, WordPress compatible, SEO-friendly, and WCAG 2.1 AA accessible.

We want a minimalist, elegant design with subtle animations, strong visuals (e.g., science/biotech imagery), and a clear structure for future growth.
Deliverables should include editable design files (Figma/Sketch/Adobe XD) and a style guide.

```html
<!DOCTYPE html>
<html lang="en">
<head>
<meta charset="utf-8">
<title>Velmora Diagnostics</title>
<link href="https://fonts.googleapis.com/css2?family=Poppins:wght@400;500;600;700&display=swap" rel="stylesheet">
<style>
:root{
  --blue:#2b8fd8;
  --blue-light:#5fb8f0;
  --blue-pale:#aee0ff;
  --navy:#1f2456;
  --navy-deep:#191d4a;
  --ink:#1c1c28;
  --muted:#5a5f6e;
  --footer-text:#c8cbe0;
  --yellow:#f6c325;
  --white:#ffffff;
}
*{box-sizing:border-box;margin:0;padding:0}
html,body{width:1200px;height:4204px;overflow:hidden}
body{font-family:"Poppins",sans-serif;color:var(--ink);background:var(--white);position:relative}
.abs{position:absolute}

.brand{left:24px;top:16px;display:flex;align-items:center;gap:10px;font-size:20px;font-weight:600;color:var(--navy)}
.brand .dot{width:22px;height:22px;border-radius:50%;background:var(--blue)}
.nav{right:24px;top:12px;display:flex;gap:24px;align-items:center;font-size:13px;font-weight:500}
.nav a{color:var(--ink);text-decoration:none}
.btn{display:inline-flex;align-items:center;gap:10px;border-radius:6px;font-size:13px;font-weight:600;color:var(--white);padding:10px 18px;text-decoration:none}
.btn-blue{background:var(--blue)}
.btn-navy{background:var(--navy)}
.btn-sky{background:var(--blue-light)}
.nav .btn{color:var(--white)}

.hero-panel{left:20px;top:70px;width:572px;height:610px;border-radius:18px;background:linear-gradient(160deg,#4aa7ea,#2b86d2 60%,#3f9be0)}
.hero-photo{left:600px;top:70px;width:580px;height:610px;border-radius:18px;background:linear-gradient(150deg,#e6eef6,#b9cde0 50%,#7a9cbc)}
.hero-title{left:60px;top:140px;width:520px;font-size:42px;line-height:1.2;font-weight:700;color:var(--white)}
.hero-title span{color:var(--blue-pale)}
.hero-sub{left:60px;top:268px;width:480px;font-size:24px;line-height:1.3;color:var(--white)}
.hero-sub .rule{display:inline-block;width:40px;height:3px;background:var(--white);vertical-align:middle;margin-right:10px}
.hero-cta{left:60px;top:390px;display:flex;gap:14px}
.proof{left:60px;top:470px;width:420px;height:110px;border-radius:12px;background:rgba(255,255,255,.92);display:flex;align-items:center;gap:18px;padding:14px}
.proof .thumb{width:150px;height:80px;border-radius:8px;background:linear-gradient(135deg,#1d4f8c,#4ea8e0)}
.proof b{font-size:22px;color:var(--navy)}
.proof small{display:block;font-size:11px;color:var(--muted)}
.avatars{display:flex;margin-left:14px}
.avatars i{width:26px;height:26px;border-radius:50%;background:#c9b8a6;border:2px solid #fff;margin-left:-8px}
.scroll-dot{left:580px;top:646px;width:40px;height:40px;border-radius:50%;background:var(--white);box-shadow:0 2px 8px rgba(0,0,0,.15)}

.section-title{left:0;width:1200px;text-align:center;font-size:34px;font-weight:700}
.section-title.blue{color:var(--blue)}
.diff{top:830px;width:280px;height:268px;border-radius:10px;background:linear-gradient(160deg,#4aa5e8,#2f8bd6);color:var(--white);text-align:center;font-size:17px;font-weight:600;padding-top:26px}
.diff .ic{width:104px;height:104px;border-radius:50%;background:rgba(255,255,255,.2);margin:0 auto 26px;display:flex;align-items:center;justify-content:center}

.kicker{left:0;width:1200px;text-align:center;font-size:20px;font-weight:700;color:var(--blue);letter-spacing:.5px}
.about-h{left:0;width:1200px;text-align:center;font-size:32px;font-weight:700;line-height:1.35}
.about-col{left:20px;top:1340px;width:440px}
.about-col h3{font-size:24px;line-height:1.3;font-weight:700;margin-bottom:10px}
.about-col p{font-size:13.5px;line-height:1.6;color:var(--muted);margin-bottom:18px}
.about-photo{left:478px;top:1340px;width:702px;height:436px;border-radius:10px;background:linear-gradient(120deg,#dfe8f0,#9fb6cb 45%,#e9eef3)}

.video{left:20px;top:1856px;width:1160px;height:514px;border-radius:10px;background:linear-gradient(110deg,#cfdbe6,#8ea9c3 40%,#e5ebf1 70%,#6f8eac)}
.play{left:570px;top:2081px;width:64px;height:64px;border-radius:50%;background:var(--yellow);display:flex;align-items:center;justify-content:center}

.trust{left:0;top:2450px;width:1200px;height:178px;background:var(--navy)}
.trust-label{left:0;top:2450px;width:255px;height:178px;background:var(--yellow);padding:46px 24px;font-size:29px;line-height:1.15;font-weight:700;color:var(--navy)}
.stat{top:2486px;width:280px;color:var(--white);text-align:center}
.stat b{display:block;font-size:58px;font-weight:600;line-height:1.1}
.stat span{font-size:16px}

.svc{top:2772px;width:280px;height:318px;border-radius:10px;overflow:hidden}
.svc .ph{height:260px}
.svc .lbl{height:58px;background:var(--blue-light);color:var(--white);font-size:15px;font-weight:600;display:flex;align-items:center;justify-content:center}

.blog{top:3232px;width:362px;height:520px;text-align:center}
.blog .ph{height:258px;border-radius:8px}
.blog .date{display:inline-block;margin-top:-14px;position:relative;background:var(--yellow);font-size:11px;font-weight:600;padding:6px 18px;border-radius:4px}
.blog h4{font-size:15px;font-weight:600;line-height:1.45;margin:22px 10px 12px}
.blog p{font-size:11.5px;line-height:1.6;color:var(--muted);margin:0 12px 22px}

.footer{left:0;top:3812px;width:1200px;height:392px;background:var(--navy-deep)}
.f-brand{left:24px;top:3840px;font-size:22px;font-weight:600;display:flex;gap:10px;align-items:center;color:var(--white)}
.f-brand .dot{width:22px;height:22px;border-radius:50%;background:var(--white)}
.f-about{left:24px;top:3900px;width:420px;font-size:12px;line-height:1.7;color:var(--footer-text)}
.f-col{color:var(--white)}
.f-col h5{font-size:12px;font-weight:600;margin-bottom:12px;letter-spacing:.5px}
.f-col a{display:block;font-size:12px;color:var(--footer-text);text-decoration:none;margin-bottom:8px}
.badge{width:80px;height:80px;border-radius:50%;border:3px solid var(--footer-text)}
.f-rule{left:24px;top:4136px;width:1152px;height:1px;background:rgba(255,255,255,.2)}
.f-bottom{left:24px;top:4156px;font-size:12px;color:var(--footer-text)}
.social{right:24px;top:4150px;display:flex;gap:10px}
.social i{width:26px;height:26px;border-radius:50%;background:var(--white)}
</style>
</head>
<body>

<header>
  <div class="abs brand"><span class="dot"></span>Velmora DX</div>
  <nav class="abs nav">
    <a href="#">HOME</a><a href="#">ABOUT US</a><a href="#">SERVICES ▾</a><a href="#">BLOG</a>
    <a class="btn btn-blue" href="#">✆ CONTACT US</a>
  </nav>
</header>

<section>
  <div class="abs hero-panel" aria-hidden="true"></div>
  <div class="abs hero-photo" role="img" aria-label="Scientist in lab coat and mask examining a sample in a bright laboratory"></div>
  <h1 class="abs hero-title"><span>Lighting</span> the Way to Early <span>Cancer Detection</span></h1>
  <p class="abs hero-sub"><span class="rule"></span>highlight non-invasive, urine-based diagnostics.</p>
  <div class="abs hero-cta">
    <a class="btn btn-navy" href="#">LEARN MORE →</a>
    <a class="btn btn-sky" href="#">CONTACT US →</a>
  </div>
  <div class="abs proof">
    <div class="thumb" role="img" aria-label="Microscope view of cells"></div>
    <div>
      <div style="display:flex;align-items:center"><b>4k +</b><div class="avatars" aria-hidden="true"><i></i><i></i><i></i></div></div>
      <small>Happy clients with positive reviews</small>
    </div>
  </div>
  <div class="abs scroll-dot" aria-hidden="true"></div>
</section>

<section>
  <h2 class="abs section-title blue" style="top:736px">KEY DIFFERENTIATORS</h2>
  <div class="abs diff" style="left:20px"><div class="ic"><svg width="56" height="56" viewBox="0 0 56 56" fill="none" stroke="#fff" stroke-width="3"><circle cx="28" cy="28" r="24"/><path d="M12 12l32 32M20 34l14-14"/></svg></div>Non-invasive,<br>painless</div>
  <div class="abs diff" style="left:315px"><div class="ic"><svg width="56" height="56" viewBox="0 0 56 56" fill="none" stroke="#fff" stroke-width="3"><path d="M18 8c0 14 20 14 20 28s-20 14-20 14M38 8c0 14-20 14-20 28s20 14 20 14M20 18h16M20 38h16"/></svg></div>Precision<br>biomarkers</div>
  <div class="abs diff" style="left:610px"><div class="ic"><svg width="56" height="56" viewBox="0 0 56 56" fill="none" stroke="#fff" stroke-width="3"><rect x="14" y="14" width="28" height="28" rx="4"/><path d="M22 6v8M34 6v8M22 42v8M34 42v8M6 22h8M6 34h8M42 22h8M42 34h8"/></svg></div>AI-powered<br>insights</div>
  <div class="abs diff" style="left:900px"><div class="ic"><svg width="56" height="56" viewBox="0 0 56 56" fill="none" stroke="#fff" stroke-width="3"><path d="M28 6l18 7v13c0 12-8 20-18 24-10-4-18-12-18-24V13z"/><path d="M19 28l7 7 12-13"/></svg></div>Clinically validated &amp;<br>university spin-out heritage</div>
</section>

<section>
  <p class="abs kicker" style="top:1162px">ABOUT US</p>
  <h2 class="abs about-h" style="top:1200px">Delivering Trusted Laboratory Testing<br>Through Scientific Expertise.</h2>
  <div class="abs about-col">
    <h3>Combining Advanced Diagnostics With Decades of Experience.</h3>
    <p>typesetting industry. Lorem Ipsum has been the industry's standard dummy text ever since the 1500s, when an unknown specimen book. It has survived not only five centuries, but also unchanged. It was popularised in the 1960s with the release more recently with desktop publishing software tools</p>
    <h3>Mission &amp; vision</h3>
    <p>typesetting industry. Lorem Ipsum has been the industry's standard dummy text ever since the 1500s, when an unknown specimen book. It has survived not only five centuries, but also unchanged. It was popularised in the 1960s with the release more recently with desktop publishing software tools</p>
    <a class="btn btn-blue" href="#">LEARN MORE →</a>
  </div>
  <div class="abs about-photo" role="img" aria-label="Collage of laboratory scientists working at microscopes and computers"></div>
</section>

<section>
  <div class="abs video" role="img" aria-label="Scientist holding a blood sample tube in a laboratory"></div>
  <div class="abs play" aria-label="Play video"><svg width="22" height="22" viewBox="0 0 22 22"><path d="M6 3l13 8-13 8z" fill="#1f2456"/></svg></div>
</section>

<section>
  <div class="abs trust" aria-hidden="true"></div>
  <div class="abs trust-label">OPTIONAL<br>TRUST TILES</div>
  <div class="abs stat" style="left:310px"><b>86%</b><span>Sensitivity</span></div>
  <div class="abs stat" style="left:600px"><b>90%</b><span>Specificity</span></div>
  <div class="abs stat" style="left:890px"><b>1,000%</b><span>Samples Validated</span></div>
</section>

<section>
  <h2 class="abs section-title" style="top:2680px">OUR SERVICES</h2>
  <div class="abs svc" style="left:20px"><div class="ph" role="img" aria-label="Anatomical view of the pancreas" style="background:linear-gradient(135deg,#f1d8cf,#d98170)"></div><div class="lbl">GlandSURE™</div></div>
  <div class="abs svc" style="left:315px"><div class="ph" role="img" aria-label="Microscope in a blue laboratory" style="background:linear-gradient(135deg,#b7c6f0,#5a6fc8)"></div><div class="lbl">Technology</div></div>
  <div class="abs svc" style="left:610px"><div class="ph" role="img" aria-label="Researchers reviewing clinical results" style="background:linear-gradient(135deg,#e8eef3,#9db4c8)"></div><div class="lbl">Science / Clinical Evidence</div></div>
  <div class="abs svc" style="left:900px"><div class="ph" role="img" aria-label="Team of partners collaborating" style="background:linear-gradient(135deg,#d7e4f1,#7da2c4)"></div><div class="lbl">Partners &amp; Collaborations</div></div>
</section>

<section>
  <h2 class="abs section-title" style="top:3150px">LATEST BLOG</h2>
  <article class="abs blog" style="left:20px"><div class="ph" role="img" aria-label="Researcher at a microscope" style="background:linear-gradient(135deg,#e4e9ef,#8ea4ba)"></div><span class="date">SEPT 22, 2025</span><h4>Lorem Ipsum is simply dummy text of the printing and typesetting industry</h4><p>Like any other industry, the construction industry has a lot to be wary of. More than just cement and paperwork errors. And it became even more conscious of safety.</p><a class="btn btn-blue" href="#">Read More →</a></article>
  <article class="abs blog" style="left:419px"><div class="ph" role="img" aria-label="Blue liquid in laboratory test tubes" style="background:linear-gradient(135deg,#cde4f7,#2f7fd0)"></div><span class="date">SEPT 22, 2025</span><h4>Lorem Ipsum is simply dummy text of the printing and typesetting industry</h4><p>Like any other industry, the construction industry has a lot to be wary of. More than just cement and paperwork errors. And it became even more conscious of safety.</p><a class="btn btn-blue" href="#">Read More →</a></article>
  <article class="abs blog" style="left:818px"><div class="ph" role="img" aria-label="Scientist holding a sample flask" style="background:linear-gradient(135deg,#e6edf4,#9fb7cd)"></div><span class="date">SEPT 22, 2025</span><h4>Lorem Ipsum is simply dummy text of the printing and typesetting industry</h4><p>Like any other industry, the construction industry has a lot to be wary of. More than just cement and paperwork errors. And it became even more conscious of safety.</p><a class="btn btn-blue" href="#">Read More →</a></article>
</section>

<footer>
  <div class="abs footer" aria-hidden="true"></div>
  <div class="abs f-brand"><span class="dot"></span>Velmora DX</div>
  <p class="abs f-about">Lorem Ipsum is simply dummy text of the printing and survived not only five centuries, but also the leap into electronic typesetting, remaining essentially unchanged. It was popularised in the 1960s with the release more recently with desktop publishing software including many versions of Lorem Ipsum.</p>
  <div class="abs f-col" style="left:500px;top:3900px"><h5>COMPLIANCE MARKERS</h5><div style="display:flex;gap:20px"><div class="badge"></div><div class="badge"></div></div></div>
  <div class="abs f-col" style="left:840px;top:3900px"><h5>QUICK LINKS</h5><a href="#">Home</a><a href="#">About</a><a href="#">Science</a><a href="#">Contact</a></div>
  <div class="abs f-col" style="left:1086px;top:3900px"><h5>LEGAL</h5><a href="#">Privacy Policy</a><a href="#">Terms of Use</a><a href="#">GDPR</a><a href="#">Accessibility</a></div>
  <div class="abs f-rule"></div>
  <p class="abs f-bottom">Velmora Diagnostics © 2025 . All rights reserved.</p>
  <div class="abs social" aria-label="Social links"><i></i><i></i><i></i></div>
</footer>

</body>
</html>
```